1 Home page redesign for existing repair service site.

We need a refresh of our existing website that looks more 2017. We have made a mockup of the content that we want and a sample of where we want it. Nothing is set in stone, if you have better ideas of where things should go, feel free.

You can see our current site at http://www.fixoloda.gr

The colors should stay orange/black/grey.

In many of the "boxes/banners" we will need images. Feel free to find in pixel vault as we have an account.

We have made notes throughout the wireframe that we have attached on what we are looking for. Let us know if you have any questions. Thanks.

Target Market(s)

People using technology and breaking it

Industry/Entity Type

It Service

Number of Pages Required

1 page

Font styles to use
Sans Serif

Requirements
Must have
• Must have a modern, professional look and feel. Need custom graphics and icons.

```html
<!DOCTYPE html>
<html lang="en">
<head>
<meta charset="utf-8">
<title>Fixoloda – Device Repair</title>
<link href="https://fonts.googleapis.com/css2?family=Roboto:wght@300;400;500;700&family=Roboto+Condensed:wght@400;700&display=swap" rel="stylesheet">
<style>
:root{
  --orange:#f26b1d;
  --orange-dark:#d9570c;
  --black:#1e1e1e;
  --dark:#2b2b2b;
  --footer:#333333;
  --grey:#6d6d6d;
  --light:#f3f3f3;
  --line:#e3e3e3;
  --white:#ffffff;
}
*{box-sizing:border-box;margin:0;padding:0}
html,body{width:1200px;height:3689px;overflow:hidden}
body{font-family:'Roboto',Arial,sans-serif;color:var(--black);background:var(--white);position:relative}
section,header,footer,div{position:relative}
.abs{position:absolute}
a{color:inherit;text-decoration:none}

/* top bar */
.topbar{height:27px;background:var(--black);color:#bbb;font-size:11px}
.quick-links{position:absolute;left:98px;top:5px;height:17px;padding:0 10px;border:1px solid #999;border-radius:9px;color:#fff;font-size:11px;line-height:15px}
.langs{position:absolute;left:826px;top:7px;font-size:10px}
.langs b{color:#fff;font-weight:500;margin-right:6px}
.socials{position:absolute;left:920px;top:9px;display:flex;gap:12px}
.socials span{width:10px;height:10px;border-radius:50%;background:#999}

/* header */
.site-header{height:96px;background:var(--white)}
.brand{position:absolute;left:98px;top:30px;display:flex;align-items:center;gap:10px}
.brand-mark{width:34px;height:34px;background:var(--orange);border-radius:4px}
.brand-name{font-size:34px;font-weight:400;color:var(--black);letter-spacing:-.5px}
.main-nav{position:absolute;left:369px;top:42px;display:flex;gap:34px;font-size:13px;color:#444}
.main-nav span{position:relative}
.main-nav .drop::after{content:"";position:absolute;left:50%;top:20px;margin-left:-4px;border:4px solid transparent;border-top-color:var(--orange)}
.main-nav .active{color:var(--orange)}
.header-phone{position:absolute;left:812px;top:40px;display:flex;align-items:center;gap:8px;font-size:20px;font-weight:400;white-space:nowrap}
.live-chat-btn{position:absolute;left:991px;top:37px;width:108px;height:34px;background:var(--orange);color:#fff;font-size:14px;font-weight:500;line-height:34px;text-align:center;border-radius:2px}
.live-chat-btn::after{content:"";position:absolute;left:20px;bottom:-8px;border:5px solid transparent;border-top-color:var(--orange)}

/* hero */
.hero{height:487px;background:linear-gradient(100deg,#c9b89b 0%,#8f8272 25%,#3a4352 45%,#8d8e8a 62%,#d7a24e 85%,#e7b760 100%)}
.hero-play{position:absolute;left:560px;top:200px}
.hero-arrow{position:absolute;top:222px}
.stat-band{height:103px;background:linear-gradient(90deg,var(--orange-dark),var(--orange) 60%,#f5842f)}
.counter{position:absolute;left:118px;top:24px;display:flex;gap:6px}
.counter span{width:57px;height:58px;background:var(--black);color:#fff;font-size:42px;font-weight:500;text-align:center;line-height:58px;font-family:'Roboto Condensed',sans-serif}
.counter span:first-child{background:#111;border:1px solid #555}
.stat-text{position:absolute;left:472px;top:39px;color:#fff;font-size:21px;font-weight:500;font-family:'Roboto Condensed',sans-serif}

/* feature tiles */
.features{height:671px}
.tile{position:absolute;overflow:hidden;color:#fff;text-align:left}
.tile .photo{position:absolute;inset:0}
.tile .shade{position:absolute;inset:0;background:rgba(0,0,0,.35)}
.tile .body{position:absolute}
.tile h3{font-size:19px;font-weight:500;line-height:1.2;text-transform:uppercase}
.tile h3.normal{text-transform:none}
.tile p{font-size:12px;line-height:1.45;margin-top:6px}
.tile .btn{display:inline-block;margin-top:10px;background:var(--orange);font-size:12px;padding:4px 10px}

/* what we repair */
.repair{height:534px;background:linear-gradient(120deg,#2b2119,#5b4535 40%,#3a2d24 70%,#1d1a18)}
.repair-card{position:absolute;left:180px;top:67px;width:838px;height:410px;background:#fff}
.repair-card h2{position:absolute;top:30px;width:100%;text-align:center;font-size:27px;font-weight:400}
.device-grid{position:absolute;left:27px;top:86px;width:791px;height:288px;display:grid;grid-template-columns:repeat(5,1fr);grid-template-rows:1fr 1fr;border:1px solid var(--line)}
.device{border-right:1px solid var(--line);border-bottom:1px solid var(--line);display:flex;flex-direction:column;align-items:center;justify-content:center;gap:18px;font-size:13px;color:#888}
.device:nth-child(5n){border-right:0}
.device:nth-child(n+6){border-bottom:0}
.device svg{height:56px}

/* options */
.section-title{position:absolute;width:100%;text-align:center;font-size:27px;font-weight:400;text-transform:uppercase}
.options{height:799px}
.option{position:absolute;top:82px;width:300px;margin-left:-150px;text-align:center}
.option .circle{width:102px;height:102px;border-radius:50%;background:var(--orange);margin:0 auto;display:flex;align-items:center;justify-content:center}
.option p{margin-top:32px;font-size:19px;color:#333}
.divider-v{position:absolute;top:82px;width:1px;height:150px;background:var(--line)}
.why-card{position:absolute;top:140px;width:248px;height:248px;overflow:hidden}
.why-card .label{position:absolute;bottom:30px;width:100%;text-align:center;color:#fff;font-size:14px;text-transform:uppercase}
.round-arrow{position:absolute;width:28px;height:28px;border:1px solid #ccc;border-radius:50%}

/* testimonials */
.testimonials{height:402px;background:var(--light)}
.stars{position:absolute;top:108px;width:100%;text-align:center;color:var(--orange);font-size:22px;letter-spacing:1px}
.quote{position:absolute;top:168px;width:290px;font-size:13px;font-style:italic;color:#555;line-height:1.55}
.quote .mark{color:#999;font-size:22px;line-height:0;vertical-align:-6px;margin-right:3px}
.author{display:flex;align-items:center;gap:18px;margin-top:26px;font-style:normal}
.avatar{width:70px;height:70px;border-radius:50%;border:3px solid #fff}
.author b{display:block;font-weight:400;color:var(--orange);font-size:13px}
.author span{color:var(--orange);font-size:13px}

/* support */
.support{height:188px;border-top:1px solid var(--line)}
.support-item{position:absolute;top:56px;display:flex;gap:20px}
.support-item h4{font-size:14px;font-weight:400;color:#222;text-transform:uppercase;margin-top:2px}
.support-item p{font-size:13px;color:#555;line-height:1.6;margin-top:6px}

/* footer */
.site-footer{height:382px;background:var(--footer);color:#ddd}
.foot-col{position:absolute;top:64px}
.foot-col h5{font-size:16px;font-weight:400;color:#fff;text-transform:uppercase;letter-spacing:.5px}
.links{list-style:none;margin-top:26px;font-size:11px;line-height:22px;color:#ccc}
.links li::before{content:"›";margin-right:12px}
.blog-post{display:flex;gap:12px;margin-top:24px}
.blog-post .thumb{width:88px;height:62px}
.blog-post p{font-size:14px;line-height:1.3;color:#fff}
.contact-line{display:flex;gap:12px;margin-top:20px;font-size:13px;line-height:1.4;color:#eee}
.newsletter{position:absolute;left:856px;top:57px;width:246px;height:108px;background:var(--orange);padding:16px 20px}
.newsletter h5{font-size:20px;font-weight:400;color:#fff;letter-spacing:1px}
.newsletter p{font-size:10px;color:#fff;margin-top:4px;line-height:1.3}
.news-form{display:flex;margin-top:10px;height:36px}
.news-form span{flex:1;background:#fff;font-size:10px;color:#999;padding-left:10px;line-height:36px}
.news-form b{width:68px;background:#222;color:#fff;font-size:9px;font-weight:500;line-height:36px;text-align:center}
.cards{position:absolute;left:944px;top:244px;display:flex;gap:8px}
.cards span{width:42px;height:24px;background:#fff;border-radius:2px;font-size:9px;font-weight:700;color:#333;text-align:center;line-height:24px}
.copyright{position:absolute;top:344px;width:100%;text-align:center;font-size:11px;color:#ccc}
</style>
</head>
<body>

<div class="topbar">
  <span class="quick-links">Quick Links ▾</span>
  <span class="langs"><b>GRE</b>ENG</span>
  <div class="socials"><span></span><span></span><span></span><span></span><span></span><span></span><span></span></div>
</div>

<header class="site-header">
  <div class="brand"><span class="brand-mark"></span><span class="brand-name">Fixoloda</span></div>
  <nav class="main-nav">
    <span class="drop active">REPAIRS</span>
    <span class="drop">20 STORES</span>
    <span>BLOG</span>
  </nav>
  <div class="header-phone">
    <svg width="26" height="20" viewBox="0 0 28 22"><path d="M2 8c0-5 24-5 24 0v3h-6V8c-3-1-9-1-12 0v3H2z" fill="#222"/><rect x="7" y="11" width="14" height="10" rx="2" fill="#222"/></svg>
    <span>2100 000 123</span>
  </div>
  <a class="live-chat-btn">LIVE CHAT</a>
</header>

<section class="hero" role="img" aria-label="Young man in glasses using his smartphone on a sunny city street">
  <svg class="hero-play" width="80" height="80" viewBox="0 0 80 80"><circle cx="40" cy="40" r="34" fill="none" stroke="#fff" stroke-width="5"/><path d="M32 25l22 15-22 15z" fill="#fff"/></svg>
  <svg class="hero-arrow" style="left:22px" width="20" height="40" viewBox="0 0 20 40"><path d="M17 2L3 20l14 18" fill="none" stroke="#fff" stroke-opacity=".6" stroke-width="2"/></svg>
  <svg class="hero-arrow" style="left:1158px" width="20" height="40" viewBox="0 0 20 40"><path d="M3 2l14 18L3 38" fill="none" stroke="#fff" stroke-opacity=".6" stroke-width="2"/></svg>
</section>

<section class="stat-band">
  <div class="counter"><span>0</span><span>1</span><span>2</span><span>3</span><span>4</span></div>
  <p class="stat-text">Repairs Completed With Happy Customers. Yep, We Fix A Lot Of Devices!</p>
</section>

<section class="features">
  <div class="tile" style="left:98px;top:69px;width:497px;height:251px">
    <div class="photo" role="img" aria-label="Technician in gloves repairing a phone" style="background:linear-gradient(135deg,#9aa0a8,#d7d9dc 45%,#5f6670)"></div>
    <div class="shade"></div>
    <div class="body" style="left:225px;top:80px;width:250px">
      <h3>20 Fixoloda locations find a store near you</h3>
      <span class="btn">View map ›</span>
    </div>
  </div>
  <div class="tile" style="left:605px;top:69px;width:497px;height:251px">
    <div class="photo" role="img" aria-label="Phone charging beside a cable on a desk" style="background:linear-gradient(135deg,#e9eaec,#b9bcc0 50%,#2f4d78)"></div>
    <div class="shade" style="background:rgba(0,0,0,.25)"></div>
    <div class="body" style="left:265px;top:80px;width:220px">
      <h3>Low price guarantee</h3>
      <p>Find a lower price for your phone or tablet repair? We will match it!</p>
    </div>
    <p class="abs" style="left:240px;top:212px;font-size:10px">*Terms and conditions apply, click to read more</p>
  </div>

  <div class="tile" style="left:98px;top:332px;width:244px;height:251px">
    <div class="photo" role="img" aria-label="Laptop on a wooden desk in an open workshop" style="background:linear-gradient(135deg,#6f7478,#9d9fa1 50%,#4a4d51)"></div>
    <div class="shade"></div>
    <div class="body" style="left:44px;top:83px;width:170px">
      <h3 class="normal">Open service area</h3>
      <p>Repairs right in front of you. No closed doors, no back rooms</p>
      <span class="btn">Read More ›</span>
    </div>
  </div>
  <div class="tile" style="left:352px;top:332px;width:245px;height:251px">
    <div class="photo" role="img" aria-label="Coffee cup and phone on a table" style="background:linear-gradient(135deg,#8a7c6e,#c9bfb3 50%,#5d544c)"></div>
    <div class="shade"></div>
    <div class="body" style="left:24px;top:75px;width:200px;text-align:center">
      <h3 class="normal">Save 50-75% on multiple repairs</h3>
      <p>If your device needs more than 1 part replaced, save up to 75% on addition parts</p>
    </div>
  </div>
  <div class="tile" style="left:605px;top:332px;width:245px;height:251px">
    <div class="photo" role="img" aria-label="Hand holding a phone and accessories" style="background:linear-gradient(135deg,#4d5660,#8c96a0 50%,#3a4048)"></div>
    <div class="shade" style="background:rgba(0,0,0,.2)"></div>
    <div class="body" style="left:0;top:196px;width:245px;text-align:center"><h3>Accessories</h3></div>
  </div>
  <div class="tile" style="left:857px;top:332px;width:245px;height:251px">
    <div class="photo" role="img" aria-label="Close-up of a phone being opened for repair" style="background:linear-gradient(135deg,#6b3a25,#b5683a 50%,#3b2218)"></div>
    <div class="shade" style="background:rgba(0,0,0,.3)"></div>
    <div class="body" style="left:20px;top:180px;width:205px;text-align:center">
      <h3 class="normal">20 minute repairs</h3>
      <p style="margin-top:4px">Most repairs can be completed in about 20 minutes</p>
    </div>
  </div>
</section>

<section class="repair" role="img" aria-label="Workbench with laptop and coffee in warm dim light">
  <div class="repair-card">
    <h2>WHAT WE REPAIR</h2>
    <div class="device-grid">
      <div class="device"><svg viewBox="0 0 28 56" width="28"><rect x="2" y="2" width="24" height="52" rx="4" fill="none" stroke="#111" stroke-width="3"/><line x1="2" y1="9" x2="26" y2="9" stroke="#111" stroke-width="2"/><line x1="2" y1="46" x2="26" y2="46" stroke="#111" stroke-width="2"/></svg>Nexaphone repair</div>
      <div class="device"><svg viewBox="0 0 44 56" width="44"><rect x="2" y="2" width="40" height="52" rx="4" fill="none" stroke="#111" stroke-width="3"/><circle cx="22" cy="49" r="2" fill="#111"/></svg>Nexatab repair</div>
      <div class="device"><svg viewBox="0 0 28 56" width="28"><rect x="2" y="2" width="24" height="52" rx="4" fill="none" stroke="#111" stroke-width="3"/><rect x="6" y="8" width="16" height="34" fill="#111"/></svg>Repair Nexapod Touch</div>
      <div class="device"><svg viewBox="0 0 30 56" width="30"><rect x="2" y="2" width="26" height="52" rx="5" fill="none" stroke="#111" stroke-width="3"/><line x1="2" y1="9" x2="28" y2="9" stroke="#111" stroke-width="2"/><line x1="2" y1="46" x2="28" y2="46" stroke="#111" stroke-width="2"/></svg>Solvane repair</div>
      <div class="device"><svg viewBox="0 0 32 56" width="32"><rect x="2" y="2" width="28" height="52" rx="5" fill="none" stroke="#111" stroke-width="3"/><rect x="6" y="7" width="20" height="18" fill="#111"/><g fill="#111"><rect x="7" y="30" width="4" height="3"/><rect x="14" y="30" width="4" height="3"/><rect x="21" y="30" width="4" height="3"/><rect x="7" y="36" width="4" height="3"/><rect x="14" y="36" width="4" height="3"/><rect x="21" y="36" width="4" height="3"/><rect x="7" y="42" width="4" height="3"/><rect x="14" y="42" width="4" height="3"/><rect x="21" y="42" width="4" height="3"/></g></svg>Keyberry repair</div>
      <div class="device"><svg viewBox="0 0 60 56" width="60"><rect x="2" y="2" width="56" height="38" fill="#111"/><rect x="2" y="40" width="56" height="6" fill="none" stroke="#111" stroke-width="2"/><path d="M24 46l-3 8h18l-3-8z" fill="#111"/></svg>repair Nexadesk</div>
      <div class="device"><svg viewBox="0 0 66 56" width="66"><rect x="10" y="10" width="46" height="32" fill="none" stroke="#111" stroke-width="3"/><path d="M2 44h62l-3 5H5z" fill="#111"/></svg>Nexabook repair</div>
      <div class="device"><svg viewBox="0 0 66 56" width="66"><rect x="2" y="6" width="44" height="32" fill="none" stroke="#111" stroke-width="3"/><path d="M18 38v8h12v-8M14 48h20" stroke="#111" stroke-width="3" fill="none"/><rect x="52" y="4" width="12" height="46" fill="#111"/></svg>Computer repair</div>
      <div class="device"><svg viewBox="0 0 66 56" width="66"><rect x="10" y="10" width="46" height="32" rx="2" fill="none" stroke="#111" stroke-width="3"/><path d="M2 44h62v3H2z" fill="#111"/></svg>Laptop repair</div>
      <div class="device"><svg viewBox="0 0 50 56" width="50"><path d="M25 8a15 15 0 0 0-9 27v6h18v-6a15 15 0 0 0-9-27z" fill="#111"/><path d="M18 45h14M20 50h10" stroke="#111" stroke-width="3"/><path d="M19 22l5 5 8-9" stroke="#fff" stroke-width="3" fill="none"/><g stroke="#111" stroke-width="3"><line x1="25" y1="0" x2="25" y2="4"/><line x1="4" y1="22" x2="0" y2="22"/><line x1="46" y1="22" x2="50" y2="22"/><line x1="9" y1="7" x2="6" y2="4"/><line x1="41" y1="7" x2="44" y2="4"/></g></svg>business Services</div>
    </div>
  </div>
</section>

<section class="options">
  <h2 class="section-title" style="top:88px">Repair Options</h2>
  <div class="divider-v" style="left:443px;top:170px"></div>
  <div class="divider-v" style="left:772px;top:170px"></div>
  <div class="option" style="left:261px;top:154px">
    <div class="circle"><svg width="52" height="36" viewBox="0 0 52 36"><path d="M2 4h30v24H2zM32 12h10l8 9v7H32z" fill="#fff"/><circle cx="12" cy="30" r="5" fill="#fff" stroke="#f26b1d" stroke-width="2"/><circle cx="40" cy="30" r="5" fill="#fff" stroke="#f26b1d" stroke-width="2"/></svg></div>
    <p>Find a store near you@</p>
  </div>
  <div class="option" style="left:600px;top:154px">
    <div class="circle"><svg width="40" height="46" viewBox="0 0 40 46"><rect x="3" y="14" width="34" height="30" fill="none" stroke="#fff" stroke-width="3"/><path d="M13 18V10a7 7 0 0 1 14 0v8" fill="none" stroke="#fff" stroke-width="3"/></svg></div>
    <p>Send us your device</p>
  </div>
  <div class="option" style="left:937px;top:154px">
    <div class="circle"><svg width="50" height="50" viewBox="0 0 50 50"><path d="M8 20a18 18 0 0 1 32-8M42 30a18 18 0 0 1-32 8" fill="none" stroke="#fff" stroke-width="3"/><path d="M40 4v9h-9M10 46v-9h9" fill="none" stroke="#fff" stroke-width="3"/><circle cx="25" cy="25" r="10" fill="#fff"/><text x="25" y="30" text-anchor="middle" font-size="13" font-weight="700" fill="#f26b1d" font-family="Roboto,sans-serif">€</text></svg></div>
    <p>Free pickup in Athens</p>
  </div>

  <h2 class="section-title" style="top:402px">Why Choose Fixoloda</h2>
  <span class="round-arrow" style="left:40px;top:592px"></span>
  <span class="round-arrow" style="left:1122px;top:592px"></span>
  <div style="position:absolute;left:0;top:325px;width:1200px;height:400px">
    <div class="why-card" style="left:98px" role="img" aria-label="Hands repairing a phone with tools"><div style="position:absolute;inset:0;background:linear-gradient(135deg,#3d3a37,#8d7d6e 55%,#2b2926)"></div><span class="label">Repairs in 20 minutes</span></div>
    <div class="why-card" style="left:350px" role="img" aria-label="Smiling woman in a yellow sweater in a workshop"><div style="position:absolute;inset:0;background:linear-gradient(135deg,#5e4a36,#b39a52 50%,#3a3026)"></div><span class="label">Low cost</span></div>
    <div class="why-card" style="left:603px" role="img" aria-label="Woman working at a repair bench"><div style="position:absolute;inset:0;background:linear-gradient(135deg,#4d3d33,#a07a63 50%,#2f2622)"></div><span class="label">Repairs parent</span></div>
    <div class="why-card" style="left:855px" role="img" aria-label="Circuit board being soldered"><div style="position:absolute;inset:0;background:linear-gradient(135deg,#1f2f2a,#5f7d6a 50%,#1c2421)"></div><span class="label">Data privacy</span></div>
  </div>
</section>

<section class="testimonials">
  <h2 class="section-title" style="top:58px">What our customers say?</h2>
  <div class="stars">★★★★★</div>
  <div class="quote" style="left:98px">
    <p><span class="mark">“</span>Lorem ipsum dolor sit amet, consectetur adipiscing elit, sed do eiusmod tempor incididunt ut labore et dolore magna aliqua Unde omnis, consequuntur.</p>
    <div class="author"><span class="avatar" role="img" aria-label="Customer portrait" style="background:linear-gradient(135deg,#e8c9a6,#b98a62)"></span><div><b>John Doe</b><span>Nexaphone 6 Repair</span></div></div>
  </div>
  <div class="quote" style="left:457px">
    <p><span class="mark">“</span>Lorem ipsum dolor sit amet, consectetur adipiscing elit, sed do eiusmod tempor incididunt ut labore et dolore magna aliqua Unde omnis, consequuntur.</p>
    <div class="author"><span class="avatar" role="img" aria-label="Customer portrait" style="background:linear-gradient(135deg,#8a6a52,#3b2c22)"></span><div><b>John Doe</b><span>Nexaphone 6 Repair</span></div></div>
  </div>
  <div class="quote" style="left:814px">
    <p><span class="mark">“</span>Lorem ipsum dolor sit amet, consectetur adipiscing elit, sed do eiusmod tempor incididunt ut labore et dolore magna aliqua Unde omnis, consequuntur.</p>
    <div class="author"><span class="avatar" role="img" aria-label="Customer portrait" style="background:linear-gradient(135deg,#e8c9a6,#b98a62)"></span><div><b>John Doe</b><span>Nexaphone 6 Repair</span></div></div>
  </div>
</section>

<section class="support">
  <div class="divider-v" style="left:443px;top:0;height:188px"></div>
  <div class="divider-v" style="left:792px;top:0;height:188px"></div>
  <div class="support-item" style="left:98px">
    <svg width="62" height="68" viewBox="0 0 62 68"><path d="M31 2l28 16v32L31 66 3 50V18z" fill="#f26b1d"/><rect x="18" y="24" width="26" height="19" fill="none" stroke="#fff" stroke-width="2.5"/><path d="M18 25l13 10 13-10" fill="none" stroke="#fff" stroke-width="2.5"/></svg>
    <div><h4>Support through E-mail</h4><p>usually respond within 24 hours<br>Send us e-mail</p></div>
  </div>
  <div class="support-item" style="left:495px">
    <svg width="62" height="68" viewBox="0 0 62 68"><path d="M31 2l28 16v32L31 66 3 50V18z" fill="#f26b1d"/><path d="M22 22c-3 2-3 6 0 11s8 10 13 12c4 1 6-1 7-3l-5-4-3 2c-3-1-7-5-8-8l2-3-4-6z" fill="#fff"/></svg>
    <div><h4>Call Center</h4><p>Talk to customer service<br>210.000.0123</p></div>
  </div>
  <div class="support-item" style="left:844px">
    <svg width="62" height="68" viewBox="0 0 62 68"><path d="M31 2l28 16v32L31 66 3 50V18z" fill="#f26b1d"/><path d="M19 36v-4a12 12 0 0 1 24 0v4" fill="none" stroke="#fff" stroke-width="3"/><rect x="16" y="34" width="7" height="10" rx="2" fill="#fff"/><rect x="39" y="34" width="7" height="10" rx="2" fill="#fff"/></svg>
    <div><h4>Live Chat</h4><p>ake a chat with a technician<br>Start the conversation</p></div>
  </div>
</section>

<footer class="site-footer">
  <div class="foot-col" style="left:98px">
    <h5>Quick Links</h5>
    <ul class="links">
      <li>About Fixoloda</li><li>Business services</li><li>Pickup from your site</li><li>Jobs</li><li>shipping information</li><li>Privacy policy</li><li>Send to ParcelNook</li>
    </ul>
  </div>
  <div class="foot-col" style="left:322px">
    <h5>Fixoloda Blog</h5>
    <div class="blog-post"><span class="thumb" role="img" aria-label="Blog post photo of a repair desk" style="background:linear-gradient(135deg,#8c6a4e,#d08a4a)"></span><p>Lorem ipsum dolor<br>consectetur adipiscing<br>06/03 2017</p></div>
    <div class="blog-post"><span class="thumb" role="img" aria-label="Blog post photo of a workshop" style="background:linear-gradient(135deg,#5b5550,#a69f97)"></span><p>Lorem ipsum dolor<br>consectetur adipiscing<br>06/03 2017</p></div>
  </div>
  <div class="foot-col" style="left:620px">
    <h5>Contacts</h5>
    <div class="contact-line"><svg width="12" height="16" viewBox="0 0 12 16"><path d="M6 0a6 6 0 0 0-6 6c0 4 6 10 6 10s6-6 6-10a6 6 0 0 0-6-6z" fill="#ddd"/><circle cx="6" cy="6" r="2" fill="#333"/></svg><span>14 Harbor Lane, Northvale,<br>Central District</span></div>
    <div class="contact-line"><svg width="12" height="14" viewBox="0 0 12 14"><path d="M2 1c-2 2-2 5 1 9s6 4 8 3l-1-3-2-1-1 1c-2-1-3-3-4-5l1-1-1-3z" fill="#ddd"/></svg><span>Phone: 0800 00 00 12</span></div>
    <div class="contact-line"><svg width="13" height="10" viewBox="0 0 13 10"><rect width="13" height="10" fill="#ddd"/><path d="M0 0l6.5 5L13 0" fill="none" stroke="#333"/></svg><span>info@fixoloda.gr</span></div>
  </div>
  <div class="newsletter">
    <h5>NEWSLETTER</h5>
    <p>Sign up for our newsletter and stay informed about repair deals</p>
    <div class="news-form"><span>E-MAIL</span><b>SUBSCRIBE</b></div>
  </div>
  <div class="cards"><span>Payvo</span><span>Amerix</span><span>Mastro</span></div>
  <p class="copyright">© 2017 Fixoloda . All Rights Reserved.</p>
</footer>

</body>
</html>
```